Valtesh Spinal Care and Performance

We need new business cards, something more modern, clean. On the back of the card maybe a quote. The Dr. likes, “The doctor of the future will give no medicine, but will interest his patient in the care of the human frame, in diet and in the cause and prevention of disease.” - Walter Pimsley. We are open to other suggestions. We are a chiropractic office.

```html
<!DOCTYPE html>
<html lang="en">
<head>
<meta charset="UTF-8">
<title>Valtesh Spinal Care and Performance – Business Card</title>
<link href="https://fonts.googleapis.com/css2?family=Bebas+Neue&display=swap" rel="stylesheet">
<style>
  :root {
    --stage: #2c3034;
    --card: #ffffff;
    --purple: #7b3a8e;
    --green: #8dba2a;
  }
  * { box-sizing: border-box; margin: 0; padding: 0; }
  html, body { width: 1200px; height: 900px; overflow: hidden; }
  body {
    background: var(--stage);
    font-family: "Bebas Neue", "Arial Narrow", sans-serif;
    position: relative;
  }
  .card {
    position: absolute;
    left: 280px;
    width: 640px;
    height: 366px;
    background: var(--card);
    border-radius: 20px;
    overflow: hidden;
    box-shadow: 0 14px 30px rgba(0,0,0,.45);
  }
  .card--front { top: 48px; }
  .card--back { top: 482px; }
  .card__edge {
    position: absolute; left: 0; right: 0; bottom: 0;
    height: 14px; background: var(--green);
  }
  .card__tab {
    position: absolute; left: 96px; bottom: 14px;
    width: 250px; height: 44px;
    background: var(--purple);
    border-radius: 22px 22px 0 0;
  }
  .brand {
    position: absolute;
    display: flex; align-items: center; gap: 12px;
  }
  .brand__dot {
    width: 18px; height: 18px; border-radius: 50%;
    background: var(--green); flex: none;
  }
  .brand__name {
    color: var(--purple);
    font-size: 34px; font-weight: 400;
    line-height: 1.02; letter-spacing: 1px;
  }
  .card--front .brand { left: 40px; top: 66px; width: 244px; }
  .card--back .brand { left: 0; right: 0; top: 44px; justify-content: center; }
  .divider {
    position: absolute; left: 300px; top: 56px;
    width: 3px; height: 200px; background: var(--purple);
  }
  .contacts {
    position: absolute; left: 334px; top: 64px;
    list-style: none;
    display: flex; flex-direction: column; gap: 14px;
  }
  .contacts__item {
    display: flex; align-items: center; gap: 16px;
    color: var(--purple); font-size: 26px; letter-spacing: 1px;
  }
  .contacts__icon {
    width: 36px; height: 36px; border-radius: 50%;
    background: var(--green);
    display: flex; align-items: center; justify-content: center;
  }
  .quote {
    position: absolute; left: 64px; right: 56px; top: 120px;
    color: var(--purple); font-size: 29px; line-height: 1.08;
    letter-spacing: .6px; text-align: center;
  }
</style>
</head>
<body>

<section class="card card--front" aria-label="Card front">
  <div class="brand">
    <span class="brand__dot"></span>
    <span class="brand__name">Valtesh Spinal Care and Performance</span>
  </div>
  <div class="divider"></div>
  <ul class="contacts">
    <li class="contacts__item">
      <span class="contacts__icon">
        <svg width="18" height="18" viewBox="0 0 18 18"><circle cx="9" cy="5.5" r="3.5" fill="#fff"/><path d="M2 17c0-4 3-6 7-6s7 2 7 6z" fill="#fff"/></svg>
      </span>Your Name
    </li>
    <li class="contacts__item">
      <span class="contacts__icon">
        <svg width="18" height="18" viewBox="0 0 18 18"><path d="M4 1.5l3 3-1.6 2a9 9 0 0 0 6 6l2-1.6 3 3-2 2.5C7.5 16.5 1.5 10.5 1.5 3.5z" fill="#fff"/></svg>
      </span>Your Phone
    </li>
    <li class="contacts__item">
      <span class="contacts__icon">
        <svg width="18" height="18" viewBox="0 0 18 18"><path d="M9 1a6 6 0 0 0-6 6c0 4.5 6 10 6 10s6-5.5 6-10a6 6 0 0 0-6-6z" fill="#fff"/><circle cx="9" cy="7" r="2.2" fill="#8dba2a"/></svg>
      </span>Your Location
    </li>
    <li class="contacts__item">
      <span class="contacts__icon">
        <svg width="18" height="18" viewBox="0 0 18 18"><rect x="1.5" y="4" width="15" height="10" rx="1" fill="#fff"/><path d="M2 4.5l7 5.5 7-5.5" fill="none" stroke="#8dba2a" stroke-width="1.4"/></svg>
      </span>Your Email
    </li>
  </ul>
  <div class="card__tab"></div>
  <div class="card__edge"></div>
</section>

<section class="card card--back" aria-label="Card back">
  <div class="brand">
    <span class="brand__dot"></span>
    <span class="brand__name">Valtesh Spinal Care and Performance</span>
  </div>
  <p class="quote">“The doctor of the future will give no medicine, but will interest his patient in the care of the human frame, in diet and in the cause and prevention of disease.”</p>
  <div class="card__tab"></div>
  <div class="card__edge"></div>
</section>

</body>
</html>
```